依頼詳細
◆サイトマップ
01.ホーム
02.当院について
03.医院紹介
04.スタッフ紹介
05.初めての方へ
06.銀歯から自然な白い歯へ
07.歯医者にいけなくなった方へ
08.歯の色を全体的に白くしたい方へ
09.口臭が気になる・歯茎に違和感がある
10.歯並びを整えたい方へ
11.歯が失ってしまった方へ
12.虫歯になってしまった方へ
13.お子様の歯を守りたい方へ
14.求人情報
15.よくあるご質問
16.問い合わせ
17.お知らせ(一覧)
18.お知らせ(詳細)
19.ブログ(一覧)
20.ブログ(詳細)

◆TOPに掲載いただきたいもの
・ヘッダー、ロゴ、営業時間、電話番号
・グローバルナビ
・メインイメージ
・お知らせの新着ボックス
・コンセプト
・強み
・各症状ページへ流入する箇所(サイトマップ06~13の内容)
・その他下層ページ移行用バナー(よくあるご質問、問い合わせ、求人情報)
・ブログの新着ボックス
・グーグルマップ
・フッター(ロゴ、院情報、営業時間、サイトマップ)
※仮で作成したもののためレイアウトの並びはお任せ致します。
ただし、配置してあるコンテンツはすべて含まれるようにしてください。
提案で項目を追加頂く等は参考にさせて頂きたいので大変嬉しいです。

◆デザインについて
・希望するイメージ
知的/清潔な/高級感

・希望デザインカラー
茶系
ベースは白やベージュ系

◆参考URL
https://hirotsudentaloffice.example/
スペースのとり方に高級感を感じとても見やすい印象
TOPのコンテンツ量が少ないと感じる
サイトURL
http://203.0.113.47
ページ数
1ページ
希望イメージ
シンプル 複雑
単色 カラフル
暗い 明るい
日常 高級
遊び心 厳粛
未来的 伝統的
女性的 男性的
希望する色
茶系、ベースは白やベージュ系
納品ファイル
• イラストレーター形式 (.ai)
• フォトショップ形式 (.psd)
補足説明
◆素材について
素材として必要なものがある場合には、Pixmora Stock画像をご使用ください。
その際、通常アセットでダウンロード出来る画像のみを使用してください。
Pixmora Stock以外の素材を使用する際には、
必ず無料で提供いただける物のみご使用ください。
※現在、写真の用意がないのですが、撮影後に差し替える予定です。
イメージとしてPixmora Stock画像を使用して作成ください。

◆ロゴ、外観、内観写真について
下記よりダウンロードしてご使用ください。
https://27.fileport-sample.example/0911-a84c27be5190f3d6e4ab07c2f9d8b3e15
PASS:qvrm
もう少し提案が見たいため、延長させて頂きます。
参考サイトを無視した少し奇抜なアイデアも見てみたいです。
■ 選んだ理由

院内で検討の上、決定致しました。
修正等も快諾いただき大変助かりました。

■ 提案者全員のお礼・コメント

皆様たくさんのご提案ありがとうございました。

```html
<!DOCTYPE html>
<html lang="ja">
<head>
<meta charset="utf-8">
<title>小森坂デンタルクリニック</title>
<link href="https://fonts.googleapis.com/css2?family=Cormorant+Garamond:wght@400;500;600&family=Noto+Serif+JP:wght@400;500;600&family=Noto+Sans+JP:wght@400;500&display=swap" rel="stylesheet">
<style>
:root{
  --cream:#fbf6ec;
  --beige:#f4ead8;
  --sand:#e8dcc5;
  --gold:#b08d57;
  --brown:#6b5236;
  --navy:#1f2b47;
  --ink:#2e2a26;
  --muted:#8a8074;
  --line:#d9cdb6;
  --white:#ffffff;
}
*{box-sizing:border-box;margin:0;padding:0}
html,body{width:1200px;height:5360px;overflow:hidden}
body{background:var(--cream);color:var(--ink);font-family:"Noto Serif JP",serif;font-size:13px;line-height:1.9}
a{text-decoration:none;color:inherit}
.serif-en{font-family:"Cormorant Garamond",serif;letter-spacing:.12em}
.sans{font-family:"Noto Sans JP",sans-serif}
section,header,footer{position:relative}
.btn{display:inline-flex;align-items:center;justify-content:center;background:var(--navy);color:var(--white);font-size:12px;letter-spacing:.1em;height:44px;width:260px;position:relative}
.btn::after{content:"";position:absolute;right:18px;top:50%;width:14px;height:1px;background:var(--white)}
.sec-title{text-align:center}
.sec-title h2{font-family:"Cormorant Garamond",serif;font-weight:500;font-size:34px;letter-spacing:.18em;color:var(--ink);line-height:1.2}
.sec-title p{font-size:11px;color:var(--gold);letter-spacing:.2em;margin-top:6px}
.ph{display:block}
/* wordmark: one colour, one weight */
.brand{display:flex;align-items:center;gap:12px;font-family:"Noto Serif JP",serif;font-weight:500;font-size:22px;letter-spacing:.12em;color:var(--ink);white-space:nowrap}
.brand i{width:14px;height:14px;background:var(--gold);display:block;flex:none}
/* header */
.site-header{height:150px;display:flex;align-items:center;padding:0 30px;background:var(--cream)}
.site-header .brand{width:340px}
.header-badges{display:flex;gap:14px;margin-left:20px}
.badge{width:120px;height:70px;border:1px solid var(--gold);display:flex;align-items:center;justify-content:center;gap:8px;font-size:11px;line-height:1.4;color:var(--brown);background:var(--white)}
.badge i{width:22px;height:22px;border-radius:50%;background:var(--gold);display:block}
.header-contact{margin-left:30px;text-align:left}
.header-contact small{font-size:11px;color:var(--muted);display:block}
.header-contact .tel{font-family:"Cormorant Garamond",serif;font-size:30px;color:var(--navy);letter-spacing:.06em;line-height:1.2}
.header-contact .tel span{font-size:18px;margin-right:6px}
.header-actions{margin-left:auto;display:flex;flex-direction:column;gap:10px}
.header-actions a{width:120px;height:40px;background:var(--navy);color:var(--white);font-size:12px;display:flex;align-items:center;justify-content:center;letter-spacing:.1em}
.global-nav{height:30px;display:flex;gap:34px;padding-left:30px;font-size:12px;color:var(--ink);align-items:center;background:var(--cream)}
/* hero */
.hero{height:300px;display:flex}
.hero-photo{width:700px;height:300px;background:linear-gradient(120deg,#efe6d4 0%,#d8c6a6 45%,#f5efe3 100%)}
.hero-copy{flex:1;padding:30px 40px;background:var(--cream)}
.hero-copy h1{font-size:26px;font-weight:500;line-height:1.65;letter-spacing:.12em;text-align:right;color:var(--ink)}
.hours{border-collapse:collapse;font-size:11px;margin-top:22px;width:100%;background:var(--white)}
.hours th,.hours td{border:1px solid var(--line);padding:4px 6px;text-align:center;font-weight:400}
.hours th{background:var(--beige)}
.hours-note{font-size:10px;color:var(--muted);margin-top:6px}
/* news */
.news{height:200px;padding:30px 80px 0 80px;display:flex;gap:60px}
.news-head h2{font-family:"Cormorant Garamond",serif;font-size:32px;font-weight:500;color:var(--ink);line-height:1}
.news-head p{font-size:11px;color:var(--gold)}
.news-list{flex:1;list-style:none;margin-top:10px}
.news-list li{border-bottom:1px solid var(--line);height:40px;display:flex;align-items:center;gap:60px;font-size:12px}
.news-list time{color:var(--muted);width:110px}
.news-more{position:absolute;left:80px;top:150px;border:1px solid var(--line);padding:4px 24px;font-size:11px;color:var(--ink);background:var(--white)}
/* greeting */
.greeting{height:760px;padding-top:120px}
.greeting-body{display:flex;gap:60px;margin:60px 0 0 170px;width:860px}
.greeting-text{flex:1}
.greeting-text h3{font-size:21px;font-weight:500;line-height:1.7;letter-spacing:.1em;margin-bottom:30px;padding-left:80px;position:relative}
.greeting-text h3::before{content:"";position:absolute;left:0;top:16px;width:64px;height:1px;background:var(--ink)}
.greeting-text p{font-size:12px;line-height:2.1;margin-bottom:16px}
.greeting-sign{text-align:right;font-size:14px;letter-spacing:.2em}
.greeting-sign small{font-size:11px;margin-right:10px}
.greeting-photo{width:230px;height:230px;flex:none;border-radius:50%;background:radial-gradient(circle at 50% 40%,#e9e2d6,#b9aea0 70%,#8d8478)}
.greeting .btn{position:absolute;left:50%;margin-left:-130px;top:630px}
/* concept */
.concept{height:900px;background:var(--beige);padding-top:80px}
.concept-lead{width:980px;margin:50px auto 0;font-size:12px;line-height:2.1}
.concept-cols{display:flex;gap:40px;width:980px;margin:60px auto 0}
.concept-col{flex:1}
.concept-col h3{font-size:22px;font-weight:500;letter-spacing:.1em;display:flex;align-items:baseline;gap:14px}
.concept-col h3 span{font-family:"Cormorant Garamond",serif;font-size:50px;line-height:1;color:var(--ink)}
.concept-col p{font-size:11px;line-height:2;margin:10px 0 20px 46px}
.concept-col .ph{height:170px}
.concept .btn{position:absolute;left:50%;margin-left:-130px;top:770px}
/* medical */
.medical{height:680px;padding-top:80px}
.medical-lead{text-align:center;font-size:13px;line-height:2;margin-top:34px}
.symptom-grid{display:grid;grid-template-columns:repeat(4,150px);gap:30px 40px;justify-content:center;margin-top:50px}
.symptom{height:130px;background:var(--white);border:1px solid var(--line);box-shadow:6px 6px 0 var(--sand);display:flex;flex-direction:column;align-items:center;justify-content:center;gap:14px;font-size:11px;line-height:1.5;text-align:center}
.symptom svg{width:36px;height:36px}
/* blog */
.blog{height:740px;padding-top:80px}
.blog-cards{display:flex;gap:40px;justify-content:center;margin-top:60px}
.blog-card{width:260px}
.blog-card .ph{height:200px}
.blog-card .meta{background:var(--white);margin:-30px 20px 0 0;position:relative;padding:14px 18px;font-size:11px}
.blog-card time{color:var(--gold);font-family:"Cormorant Garamond",serif;font-size:14px;display:block}
.blog .btn{position:absolute;left:50%;margin-left:-130px;top:560px}
/* access */
.access{height:680px;padding-top:60px}
.access-body{display:flex;gap:60px;width:1000px;margin:50px auto 0}
.access-info{width:340px}
.access-info .tel{font-family:"Cormorant Garamond",serif;font-size:30px;color:var(--navy);display:flex;align-items:center;gap:10px}
.access-info .addr{font-size:12px;margin:10px 0 18px}
.access-info .hours{width:330px}
.access-info .note{font-size:11px;line-height:2;margin-top:14px}
.access-map{flex:1;height:400px;background:linear-gradient(135deg,#e6e8ec,#d3d8df 60%,#e9ecef)}
/* exterior + banners */
.exterior{height:440px;background:linear-gradient(180deg,#3d4656 0%,#5d6573 40%,#2a2d33 100%)}
.banners{position:absolute;left:50%;margin-left:-500px;top:290px;display:flex;gap:30px}
.banner{width:313px;height:130px;background:var(--navy);border:1px solid var(--gold);outline:6px solid rgba(31,43,71,.6);display:flex;flex-direction:column;align-items:center;justify-content:center;color:var(--white)}
.banner strong{font-family:"Cormorant Garamond",serif;font-size:26px;font-weight:500;letter-spacing:.16em}
.banner span{font-size:11px;letter-spacing:.2em}
/* footer */
.site-footer{height:480px;background:var(--cream);padding:40px 0 0 300px;display:flex;gap:70px}
.foot-col h4{font-size:13px;font-weight:500;margin-bottom:8px}
.foot-col ul{list-style:none;font-size:11px;line-height:2}
.foot-col li::before{content:"・"}
.foot-brand{position:absolute;left:30px;top:330px}
.copy{position:absolute;right:40px;bottom:18px;font-size:10px;color:var(--muted)}
</style>
</head>
<body>

<header class="site-header">
  <div class="brand"><i></i>小森坂デンタルクリニック</div>
  <div class="header-badges">
    <div class="badge"><i></i>土曜日も<br>午後診療</div>
    <div class="badge"><i></i>女性歯科医師<br>在籍</div>
  </div>
  <div class="header-contact">
    <small>土曜日も午後まで診療・ご予約はこちら</small>
    <div class="tel"><span>Tel</span>090-4512-6083</div>
    <small>広島県尾道市 小森坂町3-12-5 駐車場完備</small>
  </div>
  <div class="header-actions">
    <a href="#">WEB予約</a>
    <a href="#">採用情報</a>
  </div>
</header>

<nav class="global-nav">
  <span>ホーム</span><span>当院について</span><span>アクセス</span><span>診療案内</span><span>お問い合わせ</span><span>求人情報</span><span>よくある質問</span>
</nav>

<section class="hero">
  <div class="hero-photo ph" role="img" aria-label="明るい院内受付の写真"></div>
  <div class="hero-copy">
    <h1>美しく健康な歯のために<br>最高峰の医療機器で<br>ワンランク上の治療を</h1>
    <table class="hours sans">
      <tr><th>診療時間</th><th>月</th><th>火</th><th>水</th><th>木</th><th>金</th><th>土</th><th>日</th></tr>
      <tr><td>9:00-12:30</td><td>●</td><td>●</td><td>●</td><td>●</td><td>●</td><td>●</td><td>―</td></tr>
      <tr><td>14:00-18:30</td><td>●</td><td>●</td><td>●</td><td>―</td><td>●</td><td>●</td><td>―</td></tr>
    </table>
    <p class="hours-note sans">休診日：木曜午後・日曜・祝日　▲土曜は17:00まで</p>
  </div>
</section>

<section class="news">
  <div class="news-head"><h2>News</h2><p>お知らせ</p></div>
  <ul class="news-list">
    <li><time>2020.9.1</time>小森坂デンタルクリニック新規オープン</li>
    <li><time>2020.8.20</time>年末年始の休診日について</li>
    <li><time>2020.8.5</time>駐車場のご案内を更新しました</li>
  </ul>
  <a class="news-more" href="#">過去のお知らせ一覧</a>
</section>

<section class="greeting">
  <div class="sec-title"><h2>GREETING</h2><p>院長ご挨拶</p></div>
  <div class="greeting-body">
    <div class="greeting-text">
      <h3>患者様に、地域に、社会に、<br>信頼できる歯科医院であり続けたい</h3>
      <p>小森坂デンタルクリニックのホームページをご覧頂きまして誠にありがとうございます。</p>
      <p>当院は地域の皆様のお口の健康を守るため、一人ひとりに寄り添った丁寧な診療を心がけております。これからも安心して通っていただける医院を目指してまいります。</p>
      <p>そして小さなお子様からご年配の方まで、ご家族みなさまが笑顔で過ごせるよう、最新の設備と確かな技術でお応えいたします。どうぞお気軽にご相談ください。</p>
      <p class="greeting-sign"><small>院長</small>森田 慎吾</p>
    </div>
    <div class="greeting-photo ph" role="img" aria-label="院長のポートレート写真"></div>
  </div>
  <a class="btn" href="#">スタッフ紹介へ</a>
</section>

<section class="concept">
  <div class="sec-title"><h2>CONCEPT</h2><p>当院のコンセプト</p></div>
  <p class="concept-lead">当院は最新のデジタル機器と確かな技術を組み合わせ、痛みの少ない丁寧な治療を追求しています。落ち着いた空間でリラックスして治療を受けていただけるよう、設備と接遇の両面から心地よさを整えました。</p>
  <div class="concept-cols">
    <div class="concept-col">
      <h3><span>1</span>最先端の技術</h3>
      <p>専門的な研修を重ねた医師が、精密な診断と治療をご提供します。</p>
      <div class="ph" style="background:linear-gradient(135deg,#cfdde6,#eef2f4)" role="img" aria-label="歯科治療の様子の写真"></div>
    </div>
    <div class="concept-col">
      <h3><span>2</span>居心地の良い空間</h3>
      <p>清潔で落ち着いた院内で、お子様連れでも安心してお過ごしいただけます。</p>
      <div class="ph" style="background:linear-gradient(135deg,#e8d6c2,#f6ece0)" role="img" aria-label="お子様とスタッフの写真"></div>
    </div>
    <div class="concept-col">
      <h3><span>3</span>安心の設備</h3>
      <p>滅菌設備や診断機器を完備し、安全性を第一に考えています。</p>
      <div class="ph" style="background:linear-gradient(135deg,#d9cfc1,#f2ece3)" role="img" aria-label="診療室の写真"></div>
    </div>
  </div>
  <a class="btn" href="#">当院について</a>
</section>

<section class="medical">
  <div class="sec-title"><h2>MEDICAL</h2><p>診療案内</p></div>
  <p class="medical-lead">下記のようなお悩みをご相談ではありませんか？<br>当院では、患者様一人一人のお悩みに寄り添った治療をご提案いたします。</p>
  <div class="symptom-grid">
    <div class="symptom">虫歯になって<br>しまった方へ<svg viewBox="0 0 36 36"><circle cx="18" cy="18" r="14" fill="none" stroke="#b08d57" stroke-width="1.5"/></svg></div>
    <div class="symptom">口臭・歯茎に<br>違和感がある方へ<svg viewBox="0 0 36 36"><circle cx="18" cy="18" r="14" fill="none" stroke="#b08d57" stroke-width="1.5"/></svg></div>
    <div class="symptom">お子様の歯を<br>守りたい方へ<svg viewBox="0 0 36 36"><circle cx="18" cy="18" r="14" fill="none" stroke="#b08d57" stroke-width="1.5"/></svg></div>
    <div class="symptom">歯を失って<br>しまった方へ<svg viewBox="0 0 36 36"><circle cx="18" cy="18" r="14" fill="none" stroke="#b08d57" stroke-width="1.5"/></svg></div>
    <div class="symptom">歯並びを<br>整えたい方へ<svg viewBox="0 0 36 36"><rect x="5" y="12" width="26" height="12" fill="none" stroke="#b08d57" stroke-width="1.5"/></svg></div>
    <div class="symptom">銀歯から自然な<br>白い歯へ<svg viewBox="0 0 36 36"><circle cx="18" cy="18" r="14" fill="none" stroke="#b08d57" stroke-width="1.5"/></svg></div>
    <div class="symptom">歯の色を全体的に<br>白くしたい方へ<svg viewBox="0 0 36 36"><circle cx="18" cy="18" r="14" fill="none" stroke="#b08d57" stroke-width="1.5"/></svg></div>
    <div class="symptom">歯医者にいけなく<br>なった方へ<svg viewBox="0 0 36 36"><path d="M18 30 L6 17 A7 7 0 0 1 18 9 A7 7 0 0 1 30 17 Z" fill="#6b5236"/></svg></div>
  </div>
</section>

<section class="blog">
  <div class="sec-title"><h2>STAFF BLOG</h2><p>ブログ</p></div>
  <div class="blog-cards">
    <article class="blog-card">
      <div class="ph" style="background:linear-gradient(135deg,#d6e8f2,#f3f8fb)" role="img" aria-label="歯の模型の写真"></div>
      <div class="meta"><time>2020.8.1</time>タイトル<br>院内の新しい設備のご紹介</div>
    </article>
    <article class="blog-card">
      <div class="ph" style="background:linear-gradient(135deg,#cfe0ea,#efe4d6)" role="img" aria-label="親子の歯みがきの写真"></div>
      <div class="meta"><time>2020.7.1</time>タイトル<br>お子様の歯みがきのコツ</div>
    </article>
    <article class="blog-card">
      <div class="ph" style="background:linear-gradient(135deg,#dcdfe2,#f4f5f6)" role="img" aria-label="歯科器具の写真"></div>
      <div class="meta"><time>2020.6.1</time>タイトル<br>定期検診の大切さについて</div>
    </article>
  </div>
  <a class="btn" href="#">過去のブログ一覧</a>
</section>

<section class="access">
  <div class="sec-title"><h2>ACCESS</h2><p>アクセス</p></div>
  <div class="access-body">
    <div class="access-info">
      <div class="tel"><svg width="22" height="22" viewBox="0 0 24 24"><path d="M6 3 L10 3 L11 8 L8.5 9.5 A11 11 0 0 0 14.5 15.5 L16 13 L21 14 L21 18 A3 3 0 0 1 18 21 A15 15 0 0 1 3 6 A3 3 0 0 1 6 3 Z" fill="#1f2b47"/></svg>090-4512-6083</div>
      <p class="addr">〒722-0046<br>広島県尾道市 小森坂町3-12-5</p>
      <table class="hours sans">
        <tr><th>診療時間</th><th>月</th><th>火</th><th>水</th><th>木</th><th>金</th><th>土</th><th>日</th></tr>
        <tr><td>9:00-12:30</td><td>●</td><td>●</td><td>●</td><td>●</td><td>●</td><td>●</td><td>―</td></tr>
        <tr><td>14:00-18:30</td><td>●</td><td>●</td><td>●</td><td>―</td><td>●</td><td>●</td><td>―</td></tr>
      </table>
      <p class="note">尾道駅から車で約10分、バス停「小森坂」より徒歩3分。<br>医院前に専用駐車場を6台ご用意しております。<br>お車でお越しの際はご利用ください。</p>
    </div>
    <div class="access-map" role="img" aria-label="医院周辺の地図"></div>
  </div>
</section>

<section class="exterior">
  <div class="ph" style="position:absolute;inset:0" role="img" aria-label="夕暮れの医院外観写真"></div>
  <div class="banners">
    <a class="banner" href="#"><strong>FAQ</strong><span>よくあるご質問</span></a>
    <a class="banner" href="#"><strong>CONTACT</strong><span>お問い合わせ</span></a>
    <a class="banner" href="#"><strong>RECRUIT</strong><span>求人情報</span></a>
  </div>
</section>

<footer class="site-footer">
  <div class="foot-col">
    <h4>当院について</h4>
    <ul><li>医院紹介</li><li>スタッフ紹介</li><li>初めての方へ</li><li>ブログ一覧</li></ul>
  </div>
  <div class="foot-col">
    <h4>診療案内</h4>
    <ul><li>銀歯から自然な白い歯へ</li><li>歯医者にいけなくなった方へ</li><li>歯の色を白くしたい方へ</li><li>口臭・歯茎の違和感</li><li>歯並びを整えたい方へ</li><li>歯を失ってしまった方へ</li><li>虫歯になってしまった方へ</li><li>お子様の歯を守りたい方へ</li></ul>
  </div>
  <div class="foot-col">
    <h4>ホーム</h4>
    <ul><li>アクセス</li><li>よくある質問</li><li>お問い合わせ</li><li>求人情報</li></ul>
  </div>
  <div class="foot-brand brand"><i></i>小森坂デンタルクリニック</div>
  <p class="copy serif-en">©2020 Komorizaka Dental All Rights Reserved.</p>
</footer>

</body>
</html>
```